Company website design for Marlowfen Pricing Counsel LLC

Design of company website. See uploaded outline. Logo hex codes for the icon colors: middle blue - 4D6C8A, dark blue - 11122B.

```html
<!DOCTYPE html>
<html lang="en">
<head>
<meta charset="utf-8">
<title>Marlowfen Pricing Counsel LLC</title>
<link href="https://fonts.googleapis.com/css2?family=Montserrat:wght@300;400;500;600;700&family=Oswald:wght@500&family=Roboto:wght@300;400;500&display=swap" rel="stylesheet">
<style>
:root{
  --blue:#4d6c8a;
  --blue-band:#4f6d8d;
  --blue-soft:#5d7a98;
  --navy:#11122b;
  --footer:#2f3f54;
  --social:#243244;
  --ink:#1f2430;
  --text:#4a4f5a;
  --muted:#9aa3ad;
  --line:#e3e6ea;
  --paper:#ffffff;
  --mist:#f4f5f7;
}
*{box-sizing:border-box;margin:0;padding:0}
html,body{width:1200px;height:4225px;overflow:hidden}
body{font-family:"Roboto",sans-serif;color:var(--text);background:var(--paper);position:relative}
.section{position:absolute;left:0;width:1200px}
h2.title{font-family:"Montserrat",sans-serif;font-weight:400;font-size:40px;color:var(--blue);text-align:center;position:absolute;left:0;width:1200px}
h2.title b{font-weight:700}
.ghost{position:absolute;left:0;width:1200px;text-align:center;font-family:"Oswald",sans-serif;font-weight:500;font-size:104px;line-height:110px;letter-spacing:1px;color:transparent;-webkit-text-stroke:1px #e9ecef;white-space:nowrap}

/* header */
.header{top:0;height:79px;background:var(--paper)}
.brand{position:absolute;left:100px;top:14px;display:flex;align-items:center;gap:10px}
.brand-mark{width:50px;height:50px;background:var(--blue)}
.brand-name{font-family:"Montserrat",sans-serif;font-weight:500;color:var(--navy);line-height:1}
.brand-name .big{font-size:32px;letter-spacing:.5px;display:block}
.brand-name .small{font-size:12px;letter-spacing:2.4px;display:block;margin-top:3px}
.menu-btn{position:absolute;right:100px;top:17px;width:98px;height:42px;background:#f2f3f5;border-radius:3px;display:flex;align-items:center;justify-content:center;gap:10px;font-family:"Montserrat",sans-serif;font-size:13px;font-weight:600;color:var(--navy)}

/* hero */
.hero{top:79px;height:624px;background:linear-gradient(180deg,#c9d7e1 0%,#b9c8d3 20%,#9a6b55 34%,#6e5a55 46%,#8b7a5c 58%,#c49a4c 70%,#a57a35 84%,#7a5a2c 100%)}
.hero-copy{position:absolute;top:220px;left:0;width:1200px;text-align:center;color:#fff}
.hero-copy .l1{font-family:"Montserrat",sans-serif;font-weight:300;font-size:42px;line-height:46px}
.hero-copy .l2{font-family:"Montserrat",sans-serif;font-weight:700;font-size:42px;line-height:48px}
.hero-copy .sub{font-size:22px;font-weight:300;margin-top:12px}
.btn{display:inline-block;background:var(--blue);color:#fff;font-family:"Montserrat",sans-serif;font-weight:600;font-size:14px;padding:15px 26px;border-radius:2px}
.hero-copy .btn{margin-top:24px}
.hero-arrow{position:absolute;top:290px}
.dots{position:absolute;top:580px;left:555px;display:flex;gap:13px}
.dots i{width:12px;height:12px;border:1.5px solid #fff;border-radius:50%;display:block}
.dots i.on{background:#fff}

/* values */
.values{top:703px;height:212px;background:var(--blue-band)}
.values h2{position:absolute;top:46px;width:1200px;text-align:center;color:#fff;font-family:"Montserrat",sans-serif;font-weight:400;font-size:40px}
.values h2 b{font-weight:700}
.value-row{position:absolute;top:122px;left:100px;width:1000px;display:flex;justify-content:space-between;align-items:center}
.value{display:flex;align-items:center;gap:7px;color:#fff;font-family:"Montserrat",sans-serif;font-size:15px;font-weight:500}
.value-sep{width:1px;height:32px;background:rgba(255,255,255,.3)}

/* services */
.services{top:915px;height:680px;background:var(--paper)}
.service{position:absolute;width:470px;display:flex;gap:22px}
.service svg{flex:none}
.service h3{font-family:"Montserrat",sans-serif;font-weight:600;font-size:17px;color:var(--navy);margin-bottom:12px}
.service p{font-size:14.5px;line-height:25px;color:var(--text)}

/* who */
.who{top:1595px;height:563px;background:var(--blue-band);overflow:hidden}
.who-title{position:absolute;left:101px;top:88px;color:#fff;font-family:"Montserrat",sans-serif;font-size:36px;line-height:44px}
.who-title .a{font-weight:400}
.who-title .b{font-weight:700;padding-left:84px;display:block}
.who-num{position:absolute;left:100px;top:295px;font-family:"Montserrat",sans-serif;font-weight:700;font-size:120px;color:#6a86a3;line-height:1}
.diamond{position:absolute;width:259px;height:259px}
.diamond .shape{position:absolute;left:38px;top:38px;width:183px;height:183px;background:var(--blue-soft);transform:rotate(45deg)}
.diamond .inner{position:absolute;inset:0;display:flex;flex-direction:column;align-items:center;justify-content:center;color:#fff;font-family:"Montserrat",sans-serif;font-weight:500;font-size:15px;text-align:center;line-height:19px;gap:8px}

/* industries */
.industries{top:2158px;height:1003px;background:var(--paper)}
.card{position:absolute;width:318px;height:341px;background:#fff;box-shadow:0 2px 8px rgba(17,18,43,.08)}
.card .photo{width:318px;height:287px}
.card .label{height:54px;display:flex;align-items:center;justify-content:center;font-family:"Montserrat",sans-serif;font-weight:500;font-size:18px;color:var(--navy)}

/* contact */
.contact{top:3161px;height:685px;background:var(--mist);overflow:hidden}
.field{position:absolute}
.field label{display:block;font-family:"Montserrat",sans-serif;font-weight:600;font-size:12.5px;color:var(--navy);margin-bottom:9px}
.field label em{color:#d9534f;font-style:normal}
.input{background:#fff;border:1px solid var(--line);height:42px;padding:0 15px;display:flex;align-items:center;font-size:13px;color:var(--muted)}
.captcha{position:absolute;left:177px;top:3723px;width:190px;height:46px;background:#f9f9f9;border:1px solid #d3d3d3;border-radius:3px;display:flex;align-items:center;padding-left:10px;gap:8px;font-size:10px;color:#333}
.captcha i{width:16px;height:16px;border:1.5px solid #c1c1c1;background:#fff;display:block}
.captcha .sq{position:absolute;right:14px;top:12px;width:20px;height:20px;background:#c8d3e6;border-radius:2px}

/* footer */
.footer{top:3846px;height:379px;background:var(--footer);color:#fff}
.fcol{position:absolute;top:85px}
.fcol h4{font-family:"Montserrat",sans-serif;font-weight:500;font-size:22px;margin-bottom:12px}
.fcol a{display:block;color:#fff;text-decoration:none;font-size:14px;line-height:32px}
.fcontact{display:flex;gap:10px;align-items:flex-start;font-size:14.5px;line-height:21px;margin-bottom:16px}
.fcontact .ic{width:38px;height:38px;border-radius:50%;background:#fff;flex:none;display:flex;align-items:center;justify-content:center}
.fbrand{position:absolute;left:765px;top:80px;display:flex;align-items:center;gap:12px}
.fbrand .mark{width:62px;height:62px;background:#fff}
.fbrand .name{font-family:"Montserrat",sans-serif;font-weight:400;line-height:1}
.fbrand .name .big{font-size:38px;display:block;letter-spacing:.5px}
.fbrand .name .small{font-size:14.5px;letter-spacing:2.6px;display:block;margin-top:6px}
.social{position:absolute;left:768px;top:196px;display:flex;gap:9px}
.social span{width:38px;height:38px;border-radius:50%;background:var(--social);display:flex;align-items:center;justify-content:center;font-family:"Montserrat",sans-serif;font-weight:600;font-size:10px;letter-spacing:.5px;color:#fff}
.copyright{position:absolute;top:326px;left:100px;width:1000px;text-align:center;font-size:13px;border-top:1px solid rgba(255,255,255,.15);padding-top:14px}
</style>
</head>
<body>

<header class="section header">
  <div class="brand">
    <div class="brand-mark"></div>
    <div class="brand-name"><span class="big">MARLOWFEN</span><span class="small">PRICING COUNSEL LLC</span></div>
  </div>
  <div class="menu-btn">MENU
    <svg width="28" height="16" viewBox="0 0 28 16"><path d="M0 1h28M7 8h21M0 15h28" stroke="#11122b" stroke-width="1.6"/></svg>
  </div>
</header>

<section class="section hero" role="img" aria-label="Photograph of a mountain range at sunrise above golden grassland with a road leading toward the peaks">
  <svg class="hero-arrow" style="left:62px" width="24" height="46" viewBox="0 0 24 46"><path d="M22 1 2 23l20 22" fill="none" stroke="#fff" stroke-width="2"/></svg>
  <svg class="hero-arrow" style="right:62px" width="24" height="46" viewBox="0 0 24 46"><path d="M2 1l20 22L2 45" fill="none" stroke="#fff" stroke-width="2"/></svg>
  <div class="hero-copy">
    <div class="l1">Building a</div>
    <div class="l2">Business is a Journey</div>
    <div class="sub">We have the valuation expertise to guide you</div>
    <span class="btn">GET STARTED</span>
  </div>
  <div class="dots"><i></i><i></i><i class="on"></i><i></i></div>
</section>

<section class="section values">
  <h2>Our <b>Values</b></h2>
  <div class="value-row">
    <div class="value"><svg width="32" height="32" viewBox="0 0 32 32" fill="none" stroke="#fff" stroke-width="1.5"><circle cx="12" cy="12" r="6"/><circle cx="21" cy="21" r="6"/><path d="M12 3v3M12 18v3M3 12h3M18 12h3"/></svg>INTEGRITY</div>
    <div class="value-sep"></div>
    <div class="value"><svg width="34" height="32" viewBox="0 0 34 32" fill="none" stroke="#fff" stroke-width="1.5"><circle cx="17" cy="12" r="8"/><path d="M3 29c2-6 8-9 14-9s12 3 14 9"/></svg>RESPONSIVENESS</div>
    <div class="value-sep"></div>
    <div class="value"><svg width="32" height="30" viewBox="0 0 32 30" fill="none" stroke="#fff" stroke-width="1.5"><path d="M2 10 8 3h16l6 7-14 17z"/><path d="M2 10h28M11 10l5 17 5-17"/></svg>EXCELLENCE</div>
    <div class="value-sep"></div>
    <div class="value"><svg width="32" height="32" viewBox="0 0 32 32" fill="none" stroke="#fff" stroke-width="1.5"><circle cx="16" cy="16" r="13"/><path d="M9 17l5 5 9-11"/></svg>RELATIONSHIPS</div>
    <div class="value-sep"></div>
    <div class="value"><svg width="32" height="30" viewBox="0 0 32 30" fill="none" stroke="#fff" stroke-width="1.5"><rect x="2" y="3" width="28" height="24"/><circle cx="11" cy="13" r="3"/><circle cx="21" cy="13" r="3"/><path d="M6 24c1-4 9-4 10 0M16 24c1-4 9-4 10 0"/></svg>COMMUNITY</div>
  </div>
</section>

<section class="section services">
  <div class="ghost" style="top:85px">OUR SERVICES</div>
  <h2 class="title" style="top:128px">What We <b>Do</b></h2>

  <div class="service" style="left:108px;top:232px">
    <svg width="74" height="72" viewBox="0 0 74 72" fill="none" stroke="#4d6c8a" stroke-width="2"><path d="M4 2h38l10 10v54H4z"/><path d="M42 2v10h10"/><text x="12" y="26" font-family="Montserrat" font-size="15" fill="#4d6c8a" stroke="none">TAX</text><path d="M12 36h28M12 44h28M12 52h20"/><circle cx="58" cy="56" r="13" fill="#fff"/><path d="M51 56l5 5 9-10"/></svg>
    <div><h3>TAX-RELATED VALUATIONS</h3><p>Valuations for estate/gift tax, charitable contributions, equity-linked compensation, corporate restructuring and insolvency purposes.</p></div>
  </div>

  <div class="service" style="left:633px;top:232px">
    <svg width="74" height="72" viewBox="0 0 74 72" fill="none" stroke="#4d6c8a" stroke-width="2"><rect x="20" y="12" width="48" height="56"/><circle cx="16" cy="16" r="12" fill="#fff"/><path d="M16 4v12h12"/><path d="M28 58l10-14 8 6 14-18"/><path d="M46 22h16M46 30h10"/></svg>
    <div><h3>FINANCIAL REPORTING</h3><p>Our work includes purchase price allocations fresh-start accounting, impairment analyses, equity-linked compensation, leases and financial instruments.”</p></div>
  </div>

  <div class="service" style="left:108px;top:410px">
    <svg width="74" height="74" viewBox="0 0 74 74" fill="none" stroke="#4d6c8a" stroke-width="2"><rect x="22" y="2" width="30" height="22" rx="2"/><path d="M28 10h18M28 16h12"/><circle cx="12" cy="34" r="6"/><circle cx="62" cy="34" r="6"/><path d="M2 72V52c0-6 4-10 10-10s10 4 10 10v20M52 72V52c0-6 4-10 10-10s10 4 10 10v20M22 56h30"/></svg>
    <div><h3>FINANCING &amp; TRANSACTION ADVISORY</h3><p>Financial assessments to evaluate debt structure &amp; capital adequacy. Valuation support for loan under-writing, capital raises, share redemptions, minority interest buyouts, buy-sell agreements as well as for mergers, acquisitions and divestitures.</p></div>
  </div>

  <div class="service" style="left:633px;top:410px">
    <svg width="74" height="72" viewBox="0 0 74 72" fill="none" stroke="#4d6c8a" stroke-width="2"><circle cx="24" cy="20" r="9"/><path d="M24 5v5M24 30v5M9 20h5M34 20h5M13 9l4 4M31 27l4 4M35 9l-4 4M13 31l4-4"/><circle cx="54" cy="10" r="4"/><circle cx="60" cy="28" r="4"/><path d="M40 20h10M44 10h6M44 28h12"/><path d="M4 56l12-8h14l10 4h-12M4 56l10 12h26l26-16c-4-4-8-3-12 0l-10 6"/></svg>
    <div><h3>BUSINESS PLANNING &amp; ADVISORY</h3><p>Outsourced financial planning and analysis (FP&amp;A) services, including model development, strategy valuation and exit options analysis.”</p></div>
  </div>
</section>

<section class="section who">
  <div class="who-title"><span class="a">Who Do</span><span class="b">We Serve</span></div>
  <div class="who-num">04</div>

  <div class="diamond" style="left:419px;top:95px"><div class="shape"></div>
    <div class="inner"><svg width="92" height="82" viewBox="0 0 92 82" fill="none" stroke="#fff" stroke-width="2.2"><circle cx="30" cy="20" r="12"/><circle cx="62" cy="20" r="12"/><path d="M8 80V52c0-10 8-18 22-18s20 8 20 14M84 80V52c0-10-8-18-22-18"/><circle cx="48" cy="56" r="8"/><path d="M34 80c0-8 6-14 14-14s14 6 14 14"/></svg>Family-Owned<br>Businesses</div></div>

  <div class="diamond" style="left:697px;top:95px"><div class="shape"></div>
    <div class="inner"><svg width="66" height="66" viewBox="0 0 66 66" fill="none" stroke="#fff" stroke-width="2.2"><path d="M2 64h62M8 64V44h8v20M22 64V34h8v20M36 64V40h8v24M50 64V24h8v40M10 32l14-12 12 8 22-18"/><circle cx="58" cy="8" r="4"/></svg>Publicly Traded<br>Companies</div></div>

  <div class="diamond" style="left:558px;top:234px"><div class="shape"></div>
    <div class="inner"><svg width="58" height="58" viewBox="0 0 58 58" fill="none" stroke="#fff" stroke-width="2.2"><circle cx="29" cy="29" r="26"/><path d="M36 20c-2-3-5-4-8-4-4 0-7 2-7 6 0 8 16 5 16 13 0 4-4 6-8 6-4 0-7-2-8-4M29 12v5M29 41v5"/></svg>Private-Equity<br>Sponsored<br>Companies</div></div>

  <div class="diamond" style="left:835px;top:237px"><div class="shape"></div>
    <div class="inner"><svg width="72" height="70" viewBox="0 0 72 70" fill="none" stroke="#fff" stroke-width="2.2"><path d="M4 18 30 4l26 14zM6 18v4h48v-4M10 24v30M50 24v10M4 58h36M2 64h38"/><path d="M34 30c-1-2-3-3-5-3-3 0-5 1-5 4 0 5 10 3 10 8 0 3-2 4-5 4s-5-1-6-3M29 24v3M29 43v3"/><rect x="44" y="38" width="10" height="28"/><rect x="56" y="46" width="12" height="20"/></svg>Lenders</div></div>
</section>

<section class="section industries">
  <div class="ghost" style="top:68px">INDUSTRIES SERVED</div>
  <h2 class="title" style="top:105px">Industries <b>Served</b></h2>

  <div class="card" style="left:100px;top:197px"><div class="photo" role="img" aria-label="Photograph of a professional working at a transparent digital display" style="background:linear-gradient(135deg,#1c2a36,#2f5a73 55%,#8fc6d6)"></div><div class="label">Technology</div></div>
  <div class="card" style="left:441px;top:197px"><div class="photo" role="img" aria-label="Photograph of orange robotic arms on a car assembly line" style="background:linear-gradient(160deg,#cfd3d8,#a9a49a 45%,#d48a2c 70%,#6f737a)"></div><div class="label">Manufacturing</div></div>
  <div class="card" style="left:782px;top:197px"><div class="photo" role="img" aria-label="Photograph of warehouse staff in safety vests packing boxes on a conveyor" style="background:linear-gradient(150deg,#c9a77c,#d9d6cf 45%,#9fa3a6 70%,#b9a07a)"></div><div class="label">Wholesale / Distribution</div></div>

  <div class="card" style="left:100px;top:563px"><div class="photo" role="img" aria-label="Photograph of colleagues meeting around laptops in a bright office" style="background:linear-gradient(160deg,#e9e6e1,#b9b2a8 45%,#4a4e58 75%,#d8d6d2)"></div><div class="label">Business &amp; Professional Services</div></div>
  <div class="card" style="left:441px;top:563px"><div class="photo" role="img" aria-label="Photograph of a shopper browsing laptops in an electronics store" style="background:linear-gradient(150deg,#e3dcd8,#c9c4c2 40%,#e26a5c 65%,#6a6e75)"></div><div class="label">Retail</div></div>
  <div class="card" style="left:782px;top:563px"><div class="photo" role="img" aria-label="Photograph of a small business owner checking a phone among shipping boxes" style="background:linear-gradient(150deg,#7b6a5a,#b99a78 45%,#5a5c62 75%,#3a3b40)"></div><div class="label">Consumer Products</div></div>
</section>

<section class="section contact">
  <div class="ghost" style="top:52px">CONTACT</div>
  <h2 class="title" style="top:88px">Contact <b>Us</b></h2>
</section>

<div class="field" style="left:177px;top:3339px;width:413px"><label>First Name<em>*</em></label><div class="input">Your Name</div></div>
<div class="field" style="left:609px;top:3339px;width:413px"><label>Email Address<em>*</em></label><div class="input">email@yourmail.com</div></div>
<div class="field" style="left:177px;top:3445px;width:845px"><label>Subject<em>*</em></label><div class="input">Subject</div></div>
<div class="field" style="left:177px;top:3549px;width:845px"><label>Comments / Questions<em>*</em></label><div class="input" style="height:122px;align-items:flex-start;padding-top:14px">Your Message</div></div>
<div class="captcha"><i></i>I'm not a robot<span class="sq"></span></div>
<span class="btn" style="position:absolute;left:384px;top:3723px;height:46px;width:181px;text-align:center;padding:15px 0;font-size:14px">SUBMIT MESSAGE</span>

<footer class="section footer">
  <div class="fcol" style="left:101px"><h4>Quick Links</h4><a>Home</a><a>Our Values</a><a>What We Do</a><a>Who Do We Serve</a><a>Industries Served</a><a>Contact Us</a></div>
  <div class="fcol" style="left:281px"><h4>Other Links</h4><a>Privacy Policy</a><a>Terms of Service</a><a>Credit</a><a>FAQ</a></div>
  <div class="fcol" style="left:464px"><h4>Contact Us</h4>
    <div class="fcontact"><span class="ic"><svg width="16" height="20" viewBox="0 0 16 20"><path d="M8 0a8 8 0 0 0-8 8c0 6 8 12 8 12s8-6 8-12a8 8 0 0 0-8-8z" fill="#4d6c8a"/><circle cx="8" cy="8" r="3" fill="#fff"/></svg></span><span>1482 W Larkhollow Rd<br>Suite 310, Boise, ID 83702</span></div>
    <div class="fcontact" style="align-items:center"><span class="ic"><svg width="18" height="18" viewBox="0 0 24 24"><path d="M6.6 10.8a15 15 0 0 0 6.6 6.6l2.2-2.2c.3-.3.7-.4 1-.2 1.1.4 2.3.6 3.6.6.6 0 1 .4 1 1V20c0 .6-.4 1-1 1A17 17 0 0 1 3 4c0-.6.4-1 1-1h3.5c.6 0 1 .4 1 1 0 1.3.2 2.5.6 3.6.1.3 0 .7-.2 1z" fill="#4d6c8a"/></svg></span><span>+1 208 555 0147</span></div>
    <div class="fcontact" style="align-items:center"><span class="ic"><svg width="18" height="14" viewBox="0 0 18 14"><rect width="18" height="14" rx="1" fill="#4d6c8a"/><path d="M1 1l8 7 8-7" fill="none" stroke="#fff" stroke-width="1.4"/></svg></span><span>hello@marlowfenpricing.com</span></div>
  </div>
  <div class="fbrand"><div class="mark"></div><div class="name"><span class="big">MARLOWFEN</span><span class="small">PRICING COUNSEL LLC</span></div></div>
  <div class="social"><span>FB</span><span>TW</span><span>LI</span><span>IG</span></div>
  <div class="copyright">Copyright © 2022 Marlowfen. All rights reserved.</div>
</footer>

</body>
</html>
```